Morvane Aesthetics Skin Care Flyer

8 1/2" x 11" three-folded brochure that will have a front panel which will show our Morvane Aesthetics logo and state that this is a Facial Menu. It might have our phone number on it and "call for appointment". The left inside flap will provide information about what we do and about the importance of facials and the rest will list services and pricing.
Updates

Brisquet Salon & Spa will not have a logo featured but it is important to show their address. Morvane Aesthetics has a newly designed logo but I am not sure how to upload it at this time. I do have a Vector file of our logo and hope to figure out the best way to make it available to all.Thank you. Added Sunday, April 26, 2015

```html
<!DOCTYPE html>
<html lang="en">
<head>
<meta charset="utf-8">
<title>Morvane Aesthetics – Facial Menu, Inside Spread</title>
<link rel="stylesheet" href="https://fonts.googleapis.com/css2?family=EB+Garamond:wght@400;600&display=swap">
<style>
  :root{
    --backdrop:#a9a9a9;
    --paper:#ffffff;
    --gold:#d8a92c;
    --gold-deep:#c4921a;
    --ochre-light:#e9c45a;
    --ochre-dark:#a9781a;
    --charcoal:#3b3a3d;
    --ink:#3a3a3a;
    --rule:#6b6b6b;
    --fold:#ececec;
  }
  *{margin:0;padding:0;box-sizing:border-box}
  html,body{width:1200px;height:1068px;overflow:hidden}
  body{background:var(--backdrop);font-family:"EB Garamond",Garamond,serif;color:var(--ink)}
  .brochure{position:absolute;left:50px;top:109px;width:1100px;height:850px;background:var(--paper);overflow:hidden;box-shadow:0 6px 20px rgba(0,0,0,.18)}
  .brochure svg{position:absolute;left:0;top:0}
  .fold{position:absolute;top:0;width:1px;height:100%;background:var(--fold)}
  .fold--one{left:367px}.fold--two{left:733px}
  .treatment-photo{position:absolute;left:880px;top:645px;width:180px;height:205px;border-radius:90px 90px 0 0;background:radial-gradient(ellipse at 50% 35%,#f3dccb 0%,#e8c2a6 45%,#d6a46f 100%)}
  .panel{position:absolute;display:flex;flex-direction:column;width:265px}
  .panel--left{left:45px;top:322px;gap:26px}
  .panel--middle{left:412px;top:238px;gap:44px}
  .panel--right{left:778px;top:190px;gap:26px}
  .service h2{font-weight:400;font-size:17px;line-height:1.15;color:var(--gold-deep);padding-bottom:5px;border-bottom:1px solid var(--rule);margin-bottom:10px}
  .service p{font-size:16px;line-height:1.42}
  .service--antiaging h2,.service--antiaging p{padding-left:24px}
  .service--products{width:250px}
</style>
</head>
<body>
<main class="brochure">
  <svg class="spa-photo" role="img" aria-label="Photo of a client relaxing with a facial mask during a spa treatment, warm golden tones" width="1100" height="320" viewBox="0 0 1100 320">
    <defs>
      <linearGradient id="photoTone" x1="0" y1="0" x2="1" y2="1">
        <stop offset="0" stop-color="var(--ochre-dark)"/>
        <stop offset=".45" stop-color="var(--ochre-light)"/>
        <stop offset="1" stop-color="var(--ochre-dark)"/>
      </linearGradient>
    </defs>
    <path d="M0,0 H1100 V165 C820,150 520,165 320,210 C190,240 90,275 0,310 Z" fill="url(#photoTone)"/>
  </svg>
  <svg class="decor" aria-hidden="true" width="1100" height="850" viewBox="0 0 1100 850">
    <path d="M0,0 H440 L0,36 Z" fill="var(--charcoal)"/>
    <path d="M0,300 C90,262 190,228 320,198 C520,153 820,140 1100,152" fill="none" stroke="var(--gold)" stroke-width="2"/>
    <path d="M0,310 C90,275 190,240 320,210 C520,165 820,150 1100,165" fill="none" stroke="var(--charcoal)" stroke-width="4"/>
    <path d="M560,850 C700,740 880,640 1100,590 V850 Z" fill="var(--gold)"/>
    <path d="M560,850 C700,740 880,640 1100,590" fill="none" stroke="var(--charcoal)" stroke-width="3"/>
  </svg>
  <div class="fold fold--one"></div>
  <div class="fold fold--two"></div>
  <div class="treatment-photo" role="img" aria-label="Portrait photo of a woman with clear, glowing skin"></div>

  <div class="panel panel--left">
    <section class="service service--classic">
      <h2>Classic European…$70.00</h2>
      <p>This revitalizing treatment begins with a deep cleansing, followed by gentle exfoliation to reveal smooth, glowing skin. A revitalizing masque, followed by a nutrient rich moisturizer, will hydrate, protect and help restore the natural balance of your skin.</p>
    </section>
    <section class="service service--antiaging">
      <h2>Anti-Aging…$80.00,<br>add a Glycolic Peel…add $20.00</h2>
      <p>A highly effective treatment for targeting visible signs of aging (fine lines, wrinkles, sun damage, etc.) and restoring a more youthful appearance. We utilize Vitamin C along with a peptide smoothing serum to produce desirable results. Add a glycolic peel for an even more efficient removal of dead skin layers while stimulating collagen production.</p>
    </section>
  </div>

  <div class="panel panel--middle">
    <section class="service service--aroma">
      <h2>Aroma Therapy…$80.00</h2>
      <p>A deep cleansing and exfoliation will restore your skin's natural radiance. The pressure point massage will stimulate blood circulation and revitalize the tissues while the wonderfully fragrant and essential oils soothe your senses and rejuvenate your skin.</p>
    </section>
    <section class="service service--acne">
      <h2>Acne Glycolic Exfoliation<br>Treatment…$95.00</h2>
      <p>Acne facials or deep cleansing facials are recommended for clients prone to oily or acneic skin or for those with uneven complexions. We incorporate a combination of thorough steaming, deep cleansing, facial extractions to remove pore-clogging sebum, and a healing mask and moisturizer. Salicylic and glycolic acids are aimed at managing and thwarting acne flare-ups.</p>
    </section>
  </div>

  <div class="panel panel--right">
    <section class="service service--sensitive">
      <h2>Sensitive Facial…$80.00</h2>
      <p>For sensitive skin, this facial utilizes gentle procedures and hypoallergenic products that are appropriate for irritation-prone skin. Those with skin sensitivities should not fear the calming effects of this delicate treatment. Facials for sensitive skin can improve complexion, reduce inflammation and boost your skin's immunity, which will help prevent future irritations.</p>
    </section>
    <section class="service service--products">
      <h2>Products</h2>
      <p>We also offer exceptional retail products that allow for further improvement between facials, when at home.</p>
    </section>
  </div>
</main>
</body>
</html>
```